Tallowmere Consulting Group Business Card Design

We have the logo we just need someone to design a modern business card design.

Name: Leopold Ganzhurt
Phone: 3052918364
Mobile: 9178402297
Web:www.tallowmereconsulting.com
email: lganzhurt@tallowmereconsulting.com
Company: Tallowmere Consulting Group
Title: CEO

Address: 718 Quenby Ave, Miami, Florida 33187

Target Market(s)

companies over 100 employees

Industry/Entity Type

Business

```html
<!DOCTYPE html>
<html lang="en">
<head>
<meta charset="utf-8">
<title>Tallowmere Consulting Group – Business Card</title>
<link rel="stylesheet" href="https://fonts.googleapis.com/css2?family=Montserrat:wght@400;500;700&display=swap">
<style>
  :root {
    --page: #d9d6d2;
    --front-bg: #ececec;
    --front-disc: #e0e0e0;
    --front-band: #4a4a4a;
    --ink: #1e1e1e;
    --ink-soft: #444;
    --rule: #9a9a9a;
    --blue: #1456f0;
    --back-bg-top: #3a3a3a;
    --back-bg-bottom: #141414;
    --back-disc: #1f1f1f;
    --back-ink: #ffffff;
    --back-ink-soft: #cfcfcf;
  }
  * { box-sizing: border-box; margin: 0; padding: 0; }
  html, body { width: 1200px; height: 960px; overflow: hidden; }
  body {
    background: var(--page);
    font-family: "Montserrat", Arial, sans-serif;
    display: flex; flex-direction: column; align-items: center; justify-content: center;
    gap: 60px;
  }
  .card {
    position: relative; width: 700px; height: 400px; overflow: hidden;
    box-shadow: 0 14px 30px rgba(0,0,0,.25);
  }
  /* front */
  .card--front { background: var(--front-bg); }
  .card--front .disc {
    position: absolute; left: 30px; top: 60px; width: 270px; height: 270px;
    border-radius: 50%; background: var(--front-disc);
  }
  .card--front .band {
    position: absolute; left: 0; right: 0; bottom: 0; height: 34px; background: var(--front-band);
  }
  .identity { position: absolute; left: 50px; top: 226px; color: var(--ink); }
  .identity .name { font-size: 26px; font-weight: 500; letter-spacing: .2px; }
  .identity .title { font-size: 14px; margin-top: 12px; color: var(--ink-soft); }
  .brand { position: absolute; display: flex; flex-direction: column; align-items: center; }
  .brand .dot { width: 58px; height: 58px; border-radius: 50%; background: var(--blue); }
  .brand .wordmark { font-weight: 700; letter-spacing: 1px; margin-top: 12px; }
  .brand .tagline { font-size: 9px; letter-spacing: 1.5px; margin-top: 2px; }
  .card--front .brand { left: 360px; width: 290px; top: 44px; color: var(--ink); }
  .card--front .brand .wordmark { font-size: 27px; }
  .contact {
    position: absolute; left: 390px; top: 176px; padding-left: 10px;
    border-left: 1px solid var(--rule);
    font-size: 11.5px; line-height: 18px; color: var(--ink);
  }
  /* back */
  .card--back { background: linear-gradient(160deg, var(--back-bg-top), var(--back-bg-bottom)); }
  .card--back .disc {
    position: absolute; right: 20px; top: 10px; width: 330px; height: 330px;
    border-radius: 50%; background: var(--back-disc); opacity: .8;
  }
  .card--back .brand { left: 0; right: 0; top: 60px; color: var(--back-ink); }
  .card--back .brand .dot { width: 70px; height: 70px; }
  .card--back .brand .wordmark { font-size: 32px; margin-top: 18px; }
  .card--back .brand .tagline { font-size: 10px; color: var(--back-ink-soft); }
  .card--back .web {
    position: absolute; left: 0; right: 0; top: 300px; text-align: center;
    font-size: 13px; font-weight: 500; color: var(--back-ink);
  }
</style>
</head>
<body>
  <section class="card card--front" aria-label="Business card front">
    <div class="disc"></div>
    <div class="band"></div>
    <div class="identity">
      <p class="name">Leopold Ganzhurt</p>
      <p class="title">CEO</p>
    </div>
    <div class="brand">
      <span class="dot"></span>
      <span class="wordmark">TALLOWMERE</span>
      <span class="tagline">CONSULTING GROUP</span>
    </div>
    <address class="contact" style="font-style:normal">
      718 Quenby Ave, Miami, Florida 33187<br>
      P: 3052918364<br>
      M: 9178402297<br>
      lganzhurt@tallowmereconsulting.com<br>
      www.tallowmereconsulting.com
    </address>
  </section>

  <section class="card card--back" aria-label="Business card back">
    <div class="disc"></div>
    <div class="brand">
      <span class="dot"></span>
      <span class="wordmark">TALLOWMERE</span>
      <span class="tagline">CONSULTING GROUP</span>
    </div>
    <p class="web">www.tallowmereconsulting.com</p>
  </section>
</body>
</html>
```